A website for Varnholt Limited

We need a new and modern website for our company. We are engineering consultants and contractors (EPC) in the oil and gas industry and building services industry.
What we do:
Engineering, procurement, construction
Automation (safety and process)
Non-destructive testing
Training
We have an existing website and the content can be referred from there since we are remaking the website
For more information visit Varnholt Limited Kenya

Coding

Number of Pages Required

1 page

```html
<!DOCTYPE html>
<html lang="en">
<head>
<meta charset="utf-8">
<title>Varnholt Limited</title>
<link href="https://fonts.googleapis.com/css2?family=Outfit:wght@300;400;500;600&display=swap" rel="stylesheet">
<style>
:root{
  --orange:#e1502b;
  --orange-light:#f0a257;
  --ink:#1f1f1f;
  --grey:#6b6b6b;
  --light:#f4f4f4;
  --dark:#1d1d1d;
  --footer:#474747;
  --white:#fff;
}
*{box-sizing:border-box;margin:0;padding:0}
html,body{width:1200px;height:3836px;overflow:hidden}
body{font-family:"Outfit",sans-serif;color:var(--ink);background:var(--white);position:relative}
section,header,footer{position:absolute;left:0;width:1200px}
.abs{position:absolute}
.pill{position:absolute;border-radius:30px;font-size:11px;display:flex;align-items:center;justify-content:center;font-weight:500}
.title{position:absolute;left:0;width:1200px;text-align:center;font-size:30px;font-weight:400}

/* header */
.site-header{top:0;height:74px;background:var(--white);border-bottom:1px solid #eee}
.logo{position:absolute;display:flex;align-items:center;gap:8px}
.logo-mark{width:40px;height:40px;border-radius:50%;background:var(--orange)}
.logo-name{font-size:15px;line-height:15px;font-weight:500;letter-spacing:.5px;text-transform:uppercase}
.nav{position:absolute;left:343px;top:29px;display:flex;gap:34px;font-size:11.5px;color:#444}
.nav .active{color:var(--orange);border-bottom:2px solid var(--orange);padding-bottom:24px}
.phone{position:absolute;left:905px;top:29px;font-size:11px;color:#333}
.btn-outline{border:1.5px solid var(--orange);color:var(--orange)}

/* hero */
.hero{top:74px;height:469px;background:linear-gradient(180deg,#5b7f9c 0%,#8a8e92 40%,#b06a4e 75%,#3c4a56 100%)}
.hero h1{position:absolute;left:200px;top:92px;font-size:44px;line-height:54px;font-weight:400;color:var(--white)}
.hero p{position:absolute;left:200px;top:210px;width:720px;font-size:17px;line-height:23px;font-weight:300;color:var(--white)}
.btn-solid{background:var(--orange);color:var(--white)}
.arrow-circle{position:absolute;width:32px;height:32px;border:1.5px solid rgba(255,255,255,.7);border-radius:50%;color:#fff;font-size:12px;display:flex;align-items:center;justify-content:center}
.tabs{position:absolute;left:613px;top:407px;width:587px;height:62px;display:flex;background:var(--white)}
.tab{flex:1;padding:16px 0 0 75px;font-size:12px;color:#333}
.tab small{display:block;font-size:9px;color:#777;margin-bottom:4px}
.tab.active{background:var(--orange);color:#fff;padding-left:37px}
.tab.active small{color:#fff}
.tabs .tab:first-child{padding-left:75px}

/* about */
.about{top:543px;height:511px}
.about-photo{position:absolute;left:200px;top:63px;width:312px;height:387px;background:linear-gradient(135deg,#8aa0b8,#45556a 60%,#c9b35a)}
.eyebrow{position:absolute;left:613px;top:101px;font-size:11px;color:var(--orange)}
.about h2{position:absolute;left:613px;top:135px;width:400px;font-size:29px;line-height:36px;font-weight:400}
.about p{position:absolute;left:613px;top:297px;width:390px;font-size:13px;line-height:22px;color:#333}
.more{position:absolute;left:613px;top:380px;padding-left:18px;border-left:2px solid var(--orange);height:30px;line-height:30px;font-size:12px;color:var(--orange)}

/* services */
.services{top:1054px;height:438px;background:var(--orange-light)}
.services .title{top:58px;color:var(--white)}
.svc-row{position:absolute;left:62px;top:116px;display:flex;gap:12px}
.card{width:205px;height:192px;background:var(--white);box-shadow:0 2px 4px rgba(0,0,0,.08)}
.card .ph{height:156px}
.card .lbl{height:36px;display:flex;align-items:center;justify-content:center;font-size:12.5px;font-weight:500}
.card.active{background:var(--orange);color:#fff}
.btn-ghost{border:1.5px solid var(--white);color:var(--white)}

/* projects */
.projects{top:1492px;height:528px}
.projects .title{top:56px}
.proj{position:absolute;top:122px;width:388px;height:280px}
.proj-lbl{position:absolute;left:50%;bottom:0;transform:translateX(-50%);background:#fff;width:290px;height:32px;border-radius:14px 14px 0 0;font-size:12px;font-weight:500;display:flex;align-items:center;justify-content:center}
.side-arrow{position:absolute;top:246px;width:32px;height:32px;border:1.5px solid var(--orange);border-radius:50%;color:var(--orange);font-size:12px;display:flex;align-items:center;justify-content:center}

/* products */
.products{top:2020px;height:437px;background:var(--orange)}
.products .title{top:54px;color:var(--white)}
.prod-row{position:absolute;left:200px;top:115px;display:flex;gap:24.6px}
.prod-row .card{width:182px;height:192px}
.prod-row .card.active{background:var(--orange-light)}

/* clients */
.clients{top:2457px;height:298px;background:linear-gradient(180deg,var(--light) 0 190px,var(--white) 190px)}
.clients .title{top:56px}
.client-row{position:absolute;left:200px;top:122px;display:flex;height:134px}
.client{width:160px;background:#fff;border-right:1.5px solid #c9c9c9;display:flex;flex-direction:column;align-items:center;padding-top:20px;font-size:12px;color:#555;text-align:center;line-height:18px}
.client:last-child{border-right:none}
.client svg{margin-bottom:12px}
.client.active{box-shadow:0 4px 14px rgba(0,0,0,.15);border-right:none}

/* partners */
.partners{top:2755px;height:275px}
.partners .title{top:18px}
.partner-strip{position:absolute;left:92px;top:81px;width:1013px;height:85px;background:#fff;box-shadow:0 6px 14px rgba(0,0,0,.08);display:flex;gap:8px;padding:8px 10px}
.partner{flex:1;border:1px solid #eee;display:flex;align-items:center;justify-content:center;gap:6px;font-size:14px;font-weight:500;color:#333}
.partner i{width:12px;height:12px;background:#999;display:inline-block}
.dots{position:absolute;top:200px;left:568px;display:flex;gap:6px}
.dots span{width:12px;height:12px;border:1.5px solid var(--orange);border-radius:50%}
.dots span.on{background:radial-gradient(var(--orange) 45%,transparent 50%)}

/* contact */
.contact{top:3030px;height:499px;background:linear-gradient(180deg,#151515,#2a2a2a)}
.contact .title{top:55px;color:var(--white)}
.info{position:absolute;top:118px;width:200px;text-align:center;color:#fff;font-size:9.5px;line-height:14px}
.info .ring{width:62px;height:62px;border:1.5px solid var(--orange);border-radius:50%;margin:0 auto 14px;display:flex;align-items:center;justify-content:center}
.field{position:absolute;background:#fff;border-radius:16px;font-size:9px;color:#444;padding:10px 18px}
.btn-send{border:1.5px solid var(--orange);color:var(--orange);background:transparent}

/* footer */
.site-footer{top:3529px;height:307px;background:var(--footer);color:#fff}
.site-footer .logo-name{font-size:19px;line-height:19px;color:#fff}
.fcol{position:absolute;top:64px;font-size:9.5px;line-height:19px;color:#e8e8e8}
.fcol h4{font-size:12px;font-weight:500;color:#fff;margin-bottom:14px}
.social{position:absolute;left:970px;width:28px;height:28px;border:1.5px solid var(--orange);border-radius:50%}
.social.on{background:var(--orange)}
.rule{position:absolute;left:200px;top:256px;width:800px;border-top:1px solid #6a6a6a}
.copy{position:absolute;top:275px;width:1200px;text-align:center;font-size:9px;color:#ddd}
.copy b{color:var(--orange);font-weight:400}
</style>
</head>
<body>

<header class="site-header">
  <div class="logo" style="left:62px;top:16px"><div class="logo-mark"></div><div class="logo-name">Varnholt<br>Limited</div></div>
  <nav class="nav">
    <span class="active">Home</span><span>About Us</span><span>Services</span><span>Products</span><span>Projects</span><span>Our Clients</span><span>Partners</span>
  </nav>
  <div class="phone">
    <svg width="10" height="10" viewBox="0 0 24 24" style="vertical-align:-1px;margin-right:4px"><path fill="#e1502b" d="M6.6 10.8a15 15 0 006.6 6.6l2.2-2.2a1 1 0 011-.25 11 11 0 003.6.6 1 1 0 011 1V20a1 1 0 01-1 1A17 17 0 013 4a1 1 0 011-1h3.5a1 1 0 011 1 11 11 0 00.6 3.6 1 1 0 01-.25 1z"/></svg>+254 700 555 018</div>
  <div class="pill btn-outline" style="left:1038px;top:22px;width:100px;height:30px">Contact Us</div>
</header>

<section class="hero" role="img" aria-label="Petroleum refinery with pipework and storage towers under a blue sky">
  <h1>To be a world class provider<br>of petroleum technical expertise.</h1>
  <p>Varnholt was incorporated in 2010 with the huge potential of the LPG and Petroleum market in Eastern and Central Africa in mind.</p>
  <div class="pill btn-solid" style="left:200px;top:277px;width:112px;height:30px">Our Products</div>
  <div class="arrow-circle" style="left:200px;top:406px">‹</div>
  <div class="arrow-circle" style="left:238px;top:406px">›</div>
  <div class="tabs">
    <div class="tab"><small>01.</small>Services</div>
    <div class="tab active"><small>02.</small>Products</div>
    <div class="tab" style="padding-left:48px"><small>03.</small>Projects</div>
  </div>
</section>

<section class="about">
  <div class="about-photo" role="img" aria-label="Engineer in a hard hat adjusting valves on a gas manifold"></div>
  <div class="eyebrow">Who We Are</div>
  <h2>Varnholt undertakes Design, Supply, Installation and Commissioning of LPG and Petroleum systems</h2>
  <p>Including LPG Reticulated Systems (piped gas). We also do LPG tank revalidation and recertification.</p>
  <div class="more">More About Our Company →</div>
</section>

<section class="services">
  <div class="title">Our services</div>
  <div class="svc-row">
    <div class="card"><div class="ph" role="img" aria-label="Technician using a tablet at a control panel" style="background:linear-gradient(135deg,#7fa0bd,#2f4a63)"></div><div class="lbl">EPC</div></div>
    <div class="card active"><div class="ph" role="img" aria-label="White LPG storage tanks" style="background:linear-gradient(135deg,#e8eef0,#7f9a7a)"></div><div class="lbl">LPG and Petroleum</div></div>
    <div class="card"><div class="ph" role="img" aria-label="Hard hat and drawings on a desk" style="background:linear-gradient(135deg,#d8d8d8,#555)"></div><div class="lbl">Engineering Consulting/ PM</div></div>
    <div class="card"><div class="ph" role="img" aria-label="Inspector testing a steel weld" style="background:linear-gradient(135deg,#9a8d7a,#3f3a34)"></div><div class="lbl">Non Destructive Testing</div></div>
    <div class="card"><div class="ph" role="img" aria-label="Workers in hi-vis vests in a factory" style="background:linear-gradient(135deg,#4a6a94,#c05a3a)"></div><div class="lbl">Training</div></div>
  </div>
  <div class="pill btn-ghost" style="left:550px;top:342px;width:100px;height:30px">Explore More</div>
</section>

<section class="projects">
  <div class="title">Our projects</div>
  <div class="side-arrow" style="left:136px">‹</div>
  <div class="proj" style="left:200px;background:linear-gradient(180deg,#2f6fb5,#8fa4b0 55%,#7b6d52)" role="img" aria-label="Steel gas pipeline running beside pine trees"><div class="proj-lbl">Piped Gas - LPG Reticulation</div></div>
  <div class="proj" style="left:612px;background:linear-gradient(180deg,#6f6aa8,#d99a9a 40%,#3d4a6a)" role="img" aria-label="Petroleum terminal with storage tanks at dusk"><div class="proj-lbl">Petroleum and LPG Terminals/ Depots</div></div>
  <div class="side-arrow" style="left:1031px">›</div>
  <div class="pill btn-outline" style="left:550px;top:448px;width:100px;height:30px">View All</div>
</section>

<section class="products">
  <div class="title">Our products</div>
  <div class="prod-row">
    <div class="card"><div class="ph" role="img" aria-label="LPG bullet tanks" style="background:linear-gradient(135deg,#e8eef0,#9aa5a8)"></div><div class="lbl">LPG</div></div>
    <div class="card active" style="color:#fff"><div class="ph" role="img" aria-label="Refinery columns" style="background:linear-gradient(180deg,#b8c8d4,#6f7a5a)"></div><div class="lbl">Petroleum</div></div>
    <div class="card"><div class="ph" role="img" aria-label="Robotic welding arms on an assembly line" style="background:linear-gradient(135deg,#8fa8c0,#3a4a5a)"></div><div class="lbl">Automation</div></div>
    <div class="card"><div class="ph" role="img" aria-label="Firefighters spraying a blaze" style="background:linear-gradient(135deg,#f4b24a,#7a3020)"></div><div class="lbl">Firefighting</div></div>
  </div>
  <div class="pill btn-ghost" style="left:550px;top:343px;width:100px;height:30px">Explore More</div>
</section>

<section class="clients">
  <div class="title">Our clients</div>
  <div class="client-row">
    <div class="client"><svg width="44" height="44" viewBox="0 0 44 44"><rect x="4" y="24" width="36" height="16" fill="#e1502b"/><rect x="10" y="10" width="6" height="14" fill="#e1502b"/><rect x="26" y="14" width="6" height="10" fill="#e1502b"/></svg>LPG/ Petroleum<br>Companies</div>
    <div class="client"><svg width="44" height="44" viewBox="0 0 44 44"><rect x="8" y="8" width="28" height="32" fill="#e1502b"/><path d="M20 14h4v4h4v4h-4v4h-4v-4h-4v-4h4z" fill="#fff"/></svg>Hospitals</div>
    <div class="client active"><svg width="44" height="44" viewBox="0 0 44 44"><rect x="4" y="18" width="36" height="8" fill="#e1502b"/><rect x="16" y="8" width="12" height="28" fill="#e1502b"/></svg>LPG Reticulation/<br>Piped Gas</div>
    <div class="client"><svg width="44" height="44" viewBox="0 0 44 44"><rect x="6" y="32" width="32" height="8" fill="#e1502b"/><path d="M14 32l6-16 12-8 3 4-10 7-5 13z" fill="#e1502b"/></svg>Industries</div>
    <div class="client"><svg width="44" height="44" viewBox="0 0 44 44"><rect x="8" y="10" width="28" height="30" fill="#e1502b"/><g fill="#fff"><rect x="12" y="14" width="5" height="5"/><rect x="20" y="14" width="5" height="5"/><rect x="28" y="14" width="5" height="5"/><rect x="12" y="23" width="5" height="5"/><rect x="20" y="23" width="5" height="5"/><rect x="28" y="23" width="5" height="5"/></g></svg>Hotels</div>
  </div>
</section>

<section class="partners">
  <div class="title">Our partners</div>
  <div class="partner-strip">
    <div class="partner"><i></i>Northgate</div>
    <div class="partner"><i></i>Plumline</div>
    <div class="partner"><i></i>Corvane Partners</div>
    <div class="partner"><i></i>Brightfold Ads</div>
    <div class="partner"><i></i>Halden Ads</div>
    <div class="partner"><i></i>Tessary Partner</div>
  </div>
  <div class="dots"><span></span><span class="on"></span><span></span><span></span></div>
</section>

<section class="contact">
  <div class="title">Contact us</div>
  <div class="info" style="left:300px"><div class="ring"><svg width="22" height="22" viewBox="0 0 24 24" fill="none" stroke="#e1502b" stroke-width="1.6"><path d="M12 22s7-7 7-12a7 7 0 00-14 0c0 5 7 12 7 12z"/><circle cx="12" cy="10" r="2.5"/></svg></div>Kestrel House, Suite 4,<br>Airport Road</div>
  <div class="info" style="left:501px"><div class="ring"><svg width="22" height="22" viewBox="0 0 24 24" fill="none" stroke="#e1502b" stroke-width="1.6"><path d="M6.6 10.8a15 15 0 006.6 6.6l2.2-2.2 4.6 1V20A17 17 0 013 4h4.2l1 4.6z"/></svg></div>Phone:<br>+254 700 555 018</div>
  <div class="info" style="left:694px"><div class="ring"><svg width="22" height="22" viewBox="0 0 24 24" fill="none" stroke="#e1502b" stroke-width="1.6"><path d="M3 10l9-6 9 6v10H3z"/><path d="M3 10l9 6 9-6"/></svg></div>Email:<br>info@varnholt.co.ke</div>
  <div class="field" style="left:307px;top:246px;width:186px;height:30px">Name</div>
  <div class="field" style="left:508px;top:246px;width:186px;height:30px">Email</div>
  <div class="field" style="left:707px;top:246px;width:186px;height:30px">Phone</div>
  <div class="field" style="left:307px;top:289px;width:586px;height:99px;border-radius:4px">Type your Message ...</div>
  <div class="pill btn-send" style="left:557px;top:403px;width:98px;height:28px">Send</div>
</section>

<footer class="site-footer">
  <div class="logo" style="left:200px;top:56px"><div class="logo-mark" style="width:52px;height:52px"></div><div class="logo-name">Varnholt<br>Limited</div></div>
  <div class="fcol" style="left:450px"><h4>Quick links</h4>Home<br>About Us<br>Services<br>Products<br>Projects<br>Our Clients<br>Partners</div>
  <div class="fcol" style="left:603px"><h4>Our services</h4>EPC<br>LPG and Petroleum<br>Engineering Consulting/ PM<br>Non Destructive Testing<br>Training</div>
  <div class="fcol" style="left:813px"><h4>Our products</h4>LPG<br>Petroleum<br>Automation<br>Firefighting</div>
  <div class="social" style="top:63px" aria-label="Social link"></div>
  <div class="social on" style="top:101px" aria-label="Social link"></div>
  <div class="social" style="top:138px" aria-label="Social link"></div>
  <svg class="abs" style="left:1089px;top:240px" width="20" height="24" viewBox="0 0 20 24"><path d="M10 0l10 24-10-6-10 6z" fill="#f0a257"/></svg>
  <div class="rule"></div>
  <div class="copy">© 2023 <b>VARNHOLT LIMITED.</b> All Right Reserved</div>
</footer>

</body>
</html>
```